Yoga Studio Postcard Advertising Flyer

Need a postcard size flyer that will promote our business. The objective is to promote location and availability. Want it to be personal. The objective to connect the audience to the purpose of yoga and the focus on enabling functional well-being. Something that is a very big focus at this point in time in the world. I really want people to see the value in connecting with us via our website, calmora app, pagewell or vibro. The colours are to be bright but not overwhelming and aligned to the logo colours. Its also important to have the location picture on the flyer - unless you think that it is way too much (try a with or without). I don't want this to be a specials brochure - it is an introduction to our brand and our business. No need to over do it with promotional lines apart from come and join us.

Delayed in organising this.

Local yogis and residence who are or want to be focused on well-being.

• Pictures - would have the logo on one side.
• Modern and aligned to website design.

```html
<!DOCTYPE html>
<html lang="en">
<head>
<meta charset="utf-8">
<title>Sable Lily Yoga – Postcard</title>
<link rel="stylesheet" href="https://fonts.googleapis.com/css2?family=Roboto:wght@300;400;500;700&family=Arimo:wght@400;700&display=swap">
<style>
  :root{
    --navy:#0d2248;
    --navy-deep:#0a1a38;
    --navy-mid:#1b3f78;
    --sky:#29a8e0;
    --sky-light:#5fc3ee;
    --ink:#3a3a3a;
    --white:#ffffff;
    --paper:#e4e4e4;
    --orange:#f58220;
    --grey:#555;
  }
  *{box-sizing:border-box;margin:0;padding:0}
  html,body{width:974px;height:1200px;overflow:hidden;background:var(--paper)}
  body{font-family:"Roboto",sans-serif}
  .canvas{position:relative;width:974px;height:1200px;overflow:hidden;background:var(--paper)}
  .card-slot{position:absolute;left:97px;width:780px;height:556px}
  .card-slot.front{top:28px}
  .card-slot.back{top:614px}
  .card{position:absolute;left:0;top:0;width:702px;height:500px;transform:scale(1.1111);transform-origin:0 0;overflow:hidden;background:var(--white);box-shadow:0 2px 6px rgba(0,0,0,.18)}
  .abs{position:absolute}
  .shapes{position:absolute;left:0;top:0;width:702px;height:500px}

  .hero-photo{position:absolute;left:0;top:0;width:702px;height:380px;
    background:linear-gradient(180deg,#9fcdf0 0%,#5aa6e0 45%,#8fbfd8 70%,#b79a74 88%,#9c8060 100%)}

  .brand{text-align:center;color:var(--navy);font-weight:300;letter-spacing:1px}
  .brand .name{font-size:23px;line-height:26px}
  .brand .sub{font-size:13px;letter-spacing:6px;color:var(--sky);line-height:18px}

  .headline{font-size:24px;font-weight:400;line-height:30px;letter-spacing:.2px}
  .headline.dark{color:var(--navy)}
  .headline.light{color:var(--white)}
  .rule{height:2px;width:130px;background:var(--sky)}

  .points{list-style:none;font-size:12.5px;line-height:13.5px;color:var(--ink)}
  .points li{position:relative;padding-left:22px;margin-bottom:6px}
  .points li svg{position:absolute;left:0;top:0}
  .vision{font-size:12.5px;font-weight:500;line-height:14px;color:var(--navy)}

  .socials{display:flex;gap:8px;align-items:center;font-size:10px;font-weight:500}
  .socials span{display:flex;align-items:center;gap:3px}
  .socials i{display:inline-block;width:9px;height:9px;border-radius:2px}
  .socials.on-dark{color:var(--white)}
  .socials.on-dark i{background:var(--sky)}
  .socials.on-light{color:var(--navy)}
  .socials.on-light i{background:var(--sky)}

  .cta{font-size:24px;font-weight:400;letter-spacing:.2px}
  .cta.light{color:var(--white)}
  .cta.dark{color:var(--navy)}

  .url-bar{background:var(--sky);color:var(--white);font-size:12px;font-weight:700;display:flex;align-items:center;gap:7px;height:27px}

  .intro{font-size:13.5px;line-height:17px;color:var(--white);font-weight:300}
  .spot{position:absolute;width:106px;height:106px;border-radius:50%;border:3px solid var(--white);box-shadow:0 0 0 2px var(--sky)}
  .spot.church{background:linear-gradient(160deg,#7db5e3,#b9b6aa 60%,#6e7a4d)}
  .spot.shore{background:linear-gradient(180deg,#5aa3e3,#9cc3e4 50%,#7a6a50)}
  .spot.studio{background:linear-gradient(180deg,#d9c8b2,#b89676 55%,#6b4a30)}

  .app-pill{border:1.5px solid var(--sky);border-radius:18px;display:flex;align-items:center;gap:8px;padding:0 8px}
  .app-pill .mark{width:20px;height:20px;border-radius:50%;background:var(--orange)}
  .app-pill .label{color:var(--orange);font-size:13px;font-weight:400}
  .store-badge{width:64px;height:22px;border-radius:4px;background:#111;border:1px solid #777}

  .address{text-align:center;color:var(--grey);font-size:12.5px;line-height:17px}
  .postal{font-family:"Arimo",sans-serif;color:#111}
  .permit{border:1px solid #444;text-align:center;font-size:13px;line-height:16.5px;padding-top:8px}
  .mail-box{border:1px solid #444}
  .mail-box .route{font-size:11px;text-align:right;padding:14px 20px 0 0}
  .mail-box .to{font-size:15.5px;line-height:18px;padding:20px 0 0 19px}
</style>
</head>
<body>
<div class="canvas">

  <!-- FRONT -->
  <div class="card-slot front">
    <section class="card card-front">
      <div class="hero-photo" role="img" aria-label="Photo of a man in a warrior yoga pose on coastal rocks under a blue sky"></div>
      <svg class="shapes" viewBox="0 0 702 500" aria-hidden="true">
        <defs>
          <linearGradient id="navyFront" x1="0" y1="0" x2="1" y2="1">
            <stop offset="0" stop-color="#1b3f78"/>
            <stop offset="1" stop-color="#0a1a38"/>
          </linearGradient>
        </defs>
        <path d="M0,225 C150,190 285,250 390,340 L333,500 L0,500 Z" fill="#ffffff"/>
        <path d="M333,500 L390,340 C470,385 610,375 702,250 L702,500 Z" fill="url(#navyFront)"/>
        <path d="M560,360 C620,340 670,300 702,250 L702,285 C670,325 620,352 560,360 Z" fill="#29a8e0"/>
        <path d="M235,245 C300,270 350,310 395,342 C480,390 620,370 702,250" fill="none" stroke="#29a8e0" stroke-width="2"/>
      </svg>

      <div class="brand abs" style="left:40px;top:112px;width:175px">
        <div class="name">SABLE LILY</div>
        <div class="sub">YOGA</div>
      </div>

      <h1 class="headline dark abs" style="left:33px;top:270px">ENABLE FUNCTIONAL<br>WELLBEING</h1>
      <div class="rule abs" style="left:33px;top:336px"></div>

      <ul class="points abs" style="left:31px;top:350px;width:330px">
        <li><svg width="12" height="12" viewBox="0 0 12 12"><circle cx="6" cy="6" r="6" fill="#29a8e0"/><path d="M3.3,6.2 L5.2,8 L8.7,4.2" fill="none" stroke="#fff" stroke-width="1.5"/></svg>Strengthen your well-being through adaptive yoga.</li>
        <li><svg width="12" height="12" viewBox="0 0 12 12"><circle cx="6" cy="6" r="6" fill="#29a8e0"/><path d="M3.3,6.2 L5.2,8 L8.7,4.2" fill="none" stroke="#fff" stroke-width="1.5"/></svg>Seek to evolve your mind and body through the challenge of yoga.</li>
        <li><svg width="12" height="12" viewBox="0 0 12 12"><circle cx="6" cy="6" r="6" fill="#29a8e0"/><path d="M3.3,6.2 L5.2,8 L8.7,4.2" fill="none" stroke="#fff" stroke-width="1.5"/></svg>Perfection is a desire and never an outcome through the practice of yoga.</li>
      </ul>
      <p class="vision abs" style="left:33px;top:446px;width:320px">Our vision is to create an atmosphere that enables inclusiveness of the whole community.</p>

      <div class="socials on-dark abs" style="right:17px;top:380px">
        <span><i></i>pagewell</span><span><i></i>calmora</span><span><i></i>vibro</span>
      </div>
      <div class="cta light abs" style="right:17px;top:405px">COME JOIN US!</div>
      <div class="url-bar abs" style="left:462px;top:443px;width:240px;padding-left:32px">
        <svg width="11" height="11" viewBox="0 0 12 12" aria-hidden="true"><circle cx="6" cy="6" r="5" fill="none" stroke="#fff" stroke-width="1"/><ellipse cx="6" cy="6" rx="2.2" ry="5" fill="none" stroke="#fff" stroke-width="1"/><path d="M1,6 H11" stroke="#fff" stroke-width="1"/></svg>
        www.sablelilyyoga.com.au
      </div>
    </section>
  </div>

  <!-- BACK -->
  <div class="card-slot back">
    <section class="card card-back">
      <svg class="shapes" viewBox="0 0 702 500" aria-hidden="true">
        <defs>
          <linearGradient id="navyBack" x1="0" y1="0" x2="1" y2="1">
            <stop offset="0" stop-color="#0a1a38"/>
            <stop offset="0.6" stop-color="#1b3f78"/>
            <stop offset="1" stop-color="#0d2248"/>
          </linearGradient>
        </defs>
        <path d="M0,0 L335,0 C300,60 305,150 345,220 C392,295 395,360 380,405 L0,405 Z" fill="url(#navyBack)"/>
        <path d="M383,290 C402,370 390,450 330,500 L352,500 C400,450 410,370 383,290 Z" fill="#29a8e0"/>
      </svg>

      <h1 class="headline light abs" style="left:33px;top:55px">ENABLE FUNCTIONAL<br>WELLBEING</h1>
      <div class="rule abs" style="left:33px;top:124px"></div>
      <p class="intro abs" style="left:33px;top:143px;width:270px">Our focus is on creating a connection to functional wellbeing through yoga, whilst having fun.</p>

      <div class="spot church" style="left:37px;top:227px" role="img" aria-label="Photo of the chapel studio building"></div>
      <div class="spot shore" style="left:137px;top:227px" role="img" aria-label="Photo of a yoga pose on the shoreline"></div>
      <div class="spot studio" style="left:240px;top:227px" role="img" aria-label="Photo of the studio interior with mats laid out"></div>

      <div class="app-pill abs" style="left:23px;top:355px;width:327px;height:35px">
        <div class="mark"></div>
        <div class="label">We are on Calmora!</div>
        <div class="store-badge" style="margin-left:6px"></div>
        <div class="store-badge"></div>
      </div>

      <div class="cta dark abs" style="left:21px;top:416px">COME JOIN US!</div>
      <div class="socials on-light abs" style="left:252px;top:425px">
        <span><i></i>pagewell</span><span><i></i>calmora</span><span><i></i>vibro</span>
      </div>
      <div class="url-bar abs" style="left:0;top:453px;width:240px;padding-left:20px">
        <svg width="11" height="11" viewBox="0 0 12 12" aria-hidden="true"><circle cx="6" cy="6" r="5" fill="none" stroke="#fff" stroke-width="1"/><ellipse cx="6" cy="6" rx="2.2" ry="5" fill="none" stroke="#fff" stroke-width="1"/><path d="M1,6 H11" stroke="#fff" stroke-width="1"/></svg>
        www.sablelilyyoga.com.au
      </div>

      <div class="brand abs" style="left:378px;top:78px;width:175px">
        <div class="name" style="font-size:19px;line-height:22px">SABLE LILY</div>
        <div class="sub" style="font-size:11px">YOGA</div>
      </div>
      <p class="address abs" style="left:370px;top:120px;width:190px">The Chapel, 214 Harbour<br>Road Kelsey NSW 2099</p>

      <div class="postal permit abs" style="left:581px;top:33px;width:102px;height:102px">
        PRSRT STD<br>ECRWSS<br>U.S. Postage<br><b>PAID</b><br>EDDM RETAIL
      </div>

      <div class="postal mail-box abs" style="left:419px;top:204px;width:264px;height:106px">
        <div class="route">******************ECRWSS****</div>
        <div class="to">Local<br>Postal Customer</div>
      </div>
    </section>
  </div>

</div>
</body>
</html>
```